Velora Pedal Journeys Brochure

We need an informational brochure designed to display all of our cycling tours for the 2019 season. The majority of text and images can be pulled from our website - www.velorapedaljourneys.com

We would like to use the colors red (#242424), Grey, and White

```html
<!DOCTYPE html>
<html lang="en">
<head>
<meta charset="utf-8">
<title>Velora Pedal Journeys Brochure</title>
<link href="https://fonts.googleapis.com/css2?family=Oswald:wght@500;700&family=Roboto:wght@400;500;700&display=swap" rel="stylesheet">
<style>
:root{
  --stage:#454545;
  --red:#7b1117;
  --red-deep:#640d12;
  --red-bright:#c8202c;
  --ink:#1f1f1f;
  --white:#ffffff;
  --soft:#f1e6e6;
}
*{box-sizing:border-box;margin:0;padding:0}
html,body{width:1200px;height:1200px;overflow:hidden;background:var(--stage);font-family:'Roboto',sans-serif;color:var(--white)}
.label{position:absolute;font-family:'Roboto',sans-serif;font-size:34px;font-weight:400;color:var(--white);letter-spacing:.5px}
.label-outside{left:55px;top:30px}
.label-inside{left:178px;top:1142px}
.spread{position:absolute;overflow:hidden;background:linear-gradient(135deg,var(--red) 0%,var(--red-deep) 100%);box-shadow:0 6px 18px rgba(0,0,0,.45)}
.spread-outside{left:53px;top:74px;width:981px;height:497px}
.spread-inside{left:180px;top:640px;width:981px;height:496px}
.abs{position:absolute}
.heading{font-family:'Oswald',sans-serif;font-weight:700;text-transform:uppercase;letter-spacing:-.3px;white-space:nowrap}
.body-copy{font-size:7.4px;line-height:13px;text-align:justify}
.body-copy p+p{margin-top:13px}
.story-title{left:23px;top:60px;font-size:18px}
.story-copy{left:23px;top:90px;width:382px}
.brand-mark{display:flex;align-items:center;gap:8px}
.brand-dot{width:46px;height:46px;border-radius:50%;border:3px solid var(--white);flex:none}
.brand-name{font-family:'Roboto',sans-serif;font-weight:700;font-size:13px;color:var(--white);line-height:1.1}
.story-brand{left:185px;top:286px;width:140px}
.contact{left:107px;top:372px;width:280px;text-align:center}
.contact-title{font-family:'Roboto',sans-serif;font-weight:500;font-size:12px;display:inline-block;padding-bottom:6px;border-bottom:1px solid rgba(255,255,255,.6)}
.contact-list{list-style:none;margin-top:24px;font-size:8.6px;line-height:16px}
.contact-list svg{width:8px;height:8px;vertical-align:-1px;margin-right:5px;fill:var(--white)}
.headline{left:604px;top:418px;font-size:36px;line-height:40px;letter-spacing:0;transform:scaleX(.88);transform-origin:left}
.url-pill{left:604px;top:463px;width:338px;height:17px;border-radius:9px;background:var(--ink);font-size:11.5px;font-weight:500;letter-spacing:2.6px;text-align:center;line-height:17px;white-space:nowrap}
.cover-brand{left:617px;top:34px}
.cover-brand .brand-dot{width:58px;height:58px;border-color:var(--red-bright);background:var(--white)}
.cover-brand .brand-name{color:var(--red-bright);font-size:22px;width:170px}
.apart-band{left:222px;top:30px;width:256px;height:54px;background:var(--white);border-radius:4px;transform:rotate(-1deg)}
.apart-title{left:222px;top:41px;width:256px;text-align:center;font-size:19px;color:var(--ink)}
.feature{position:absolute;left:254px;width:222px}
.feature-head{display:flex;align-items:center;gap:8px;font-weight:500;font-size:14.5px;text-transform:uppercase;white-space:nowrap}
.feature-icon{width:24px;height:24px;border-radius:50%;background:var(--white);display:flex;align-items:center;justify-content:center;flex:none}
.feature-icon svg{width:14px;height:14px;stroke:var(--red);fill:none;stroke-width:2}
.feature .body-copy{margin-top:12px;font-size:7.4px;line-height:11px}
.inside-url{left:218px;top:442px;font-size:9px;white-space:nowrap}
.inside-brand{left:407px;top:420px}
.inside-brand .brand-dot{width:58px;height:58px}
.panel{left:486px;top:0;width:495px;height:496px;background:linear-gradient(160deg,#7e1218 0%,#6a0e14 100%)}
.section-title{font-size:16px;left:511px}
.section-copy{left:511px;width:455px;font-size:7.4px;line-height:11px}
.rule{left:511px;width:125px;height:1px;background:rgba(255,255,255,.5)}
.bike-name{left:511px;font-weight:500;font-size:11.5px}
.bike-name::before{content:"";position:absolute;left:2px;top:-3px;width:4px;height:4px;border-radius:50%;background:var(--white)}
.bike-name span{padding-left:12px}
.specs{left:511px;list-style:none;font-weight:700;font-size:9px;line-height:12.4px;text-transform:uppercase}
.specs li{position:relative;padding-left:8px}
.specs li::before{content:"";position:absolute;left:1px;top:2px;width:2px;height:2px;border-radius:50%;background:var(--white)}
.bike-photo{left:812px;width:76px;height:76px;border-radius:50%;border:3px solid var(--white);background:radial-gradient(circle,#ffffff 55%,#dcdcdc 100%);box-shadow:0 2px 6px rgba(0,0,0,.4)}
</style>
</head>
<body>

<div class="label label-outside">OUTSIDE BROCHURE</div>

<section class="spread spread-outside">
  <h2 class="abs heading story-title">Our Story</h2>
  <div class="abs body-copy story-copy">
    <p>Velora Pedal Journeys was born from decades of experience as North America's leading specialist tour operator and a lifelong passion for cycling and mountain biking. We wanted to create a series of tours made for bikers by bikers, that highlight not only the most famous rides in the country, but also our favorites.</p>
    <p>While we have some amazing colleagues in the industry, we've found many tours to be slowed down by lazy days and charcuterie. While there's always time for cold, hazy IPA's and bold Cabernets, we find they taste better after cruising some of the most incredible rides of your life. Our mantra, "It's all about the ride," emphasizes our desire to create unique itineraries that will test your abilities, and help you find your strongest flow.</p>
    <p>Velora Pedal Journeys is where passion meets experience.</p>
  </div>

  <div class="abs brand-mark story-brand">
    <span class="brand-dot"></span>
    <span class="brand-name">Velora Pedal<br>Journeys</span>
  </div>

  <div class="abs contact">
    <div class="contact-title">GET IN TOUCH</div>
    <ul class="contact-list">
      <li><svg viewBox="0 0 10 10"><path d="M5 0a3.5 3.5 0 0 0-3.5 3.5C1.5 6 5 10 5 10s3.5-4 3.5-6.5A3.5 3.5 0 0 0 5 0zm0 5a1.4 1.4 0 1 1 0-2.8A1.4 1.4 0 0 1 5 5z"/></svg>214 Orchard Lane, Alder Falls, California</li>
      <li><svg viewBox="0 0 10 10"><path d="M2 0l2 2.4-1.2 1.3a6 6 0 0 0 3.5 3.5L7.6 6 10 8l-1.5 2C4 10 0 6 0 1.5z"/></svg>+1 555-014-2290</li>
      <li><svg viewBox="0 0 10 10"><path d="M0 2h10v6H0zM.8 2.6 5 5.6l4.2-3" fill="none" stroke="#fff" stroke-width="1"/></svg>ride@velorapedaljourneys.com</li>
      <li><svg viewBox="0 0 10 10"><circle cx="5" cy="5" r="4.3" fill="none" stroke="#fff" stroke-width="1.2"/><path d="M.7 5h8.6M5 .7c2 2.6 2 6 0 8.6M5 .7c-2 2.6-2 6 0 8.6" fill="none" stroke="#fff" stroke-width=".8"/></svg>www.velorapedaljourneys.com</li>
    </ul>
  </div>

  <svg class="abs" style="left:0;top:0" width="981" height="497" viewBox="0 0 981 497">
    <defs>
      <linearGradient id="cover-photo" x1="0" y1="0" x2="0" y2="1">
        <stop offset="0" stop-color="#b9c8de"/>
        <stop offset=".45" stop-color="#d7dde4"/>
        <stop offset=".62" stop-color="#3f5a34"/>
        <stop offset=".85" stop-color="#6b4a34"/>
        <stop offset="1" stop-color="#7a2c22"/>
      </linearGradient>
      <linearGradient id="inset-a" x1="0" y1="0" x2="0" y2="1">
        <stop offset="0" stop-color="#c7d3dd"/><stop offset=".55" stop-color="#8b8878"/><stop offset="1" stop-color="#6f624f"/>
      </linearGradient>
      <linearGradient id="inset-b" x1="0" y1="0" x2="0" y2="1">
        <stop offset="0" stop-color="#8fae6a"/><stop offset=".6" stop-color="#4f6a3a"/><stop offset="1" stop-color="#7a6a4e"/>
      </linearGradient>
    </defs>
    <path d="M600 0 C560 90 535 220 539 326 C543 410 570 460 595 497 H981 V0Z" fill="#1f1f1f"/>
    <path role="img" aria-label="Photo of a mountain biker riding a red dirt trail through pine forest" d="M614 0 C575 90 550 220 554 326 C558 410 585 460 610 497 H981 V0Z" fill="url(#cover-photo)"/>
    <circle cx="520" cy="190" r="102" fill="none" stroke="rgba(255,255,255,.6)" stroke-width="1"/>
    <circle cx="559" cy="283" r="77" fill="none" stroke="rgba(255,255,255,.6)" stroke-width="1"/>
    <circle role="img" aria-label="Photo of a rider standing beside his bike at a coastal lookout" cx="523" cy="165" r="84" fill="url(#inset-a)" stroke="#fff" stroke-width="4"/>
    <circle role="img" aria-label="Photo of a rider on a mountain bike in a green meadow" cx="559" cy="285" r="54" fill="url(#inset-b)" stroke="#fff" stroke-width="4"/>
  </svg>

  <div class="abs brand-mark cover-brand">
    <span class="brand-dot"></span>
    <span class="brand-name">Velora Pedal Journeys</span>
  </div>

  <h1 class="abs heading headline">It's all about the ride</h1>
  <div class="abs url-pill">www.velorapedaljourneys.com</div>
</section>

<section class="spread spread-inside">
  <svg class="abs" style="left:0;top:0" width="486" height="496" viewBox="0 0 486 496">
    <defs>
      <linearGradient id="trail-photo" x1="0" y1="0" x2="0" y2="1">
        <stop offset="0" stop-color="#6f7a44"/>
        <stop offset=".4" stop-color="#b59a4a"/>
        <stop offset=".7" stop-color="#7a5a36"/>
        <stop offset="1" stop-color="#2a2420"/>
      </linearGradient>
    </defs>
    <path d="M0 0 H190 C235 110 250 230 236 330 C226 400 205 450 185 496 H0Z" fill="#1f1f1f"/>
    <path role="img" aria-label="Photo of a cyclist on a dirt singletrack at golden hour, seen from behind the handlebars" d="M0 0 H178 C222 110 236 230 222 330 C212 400 192 450 172 496 H0Z" fill="url(#trail-photo)"/>
    <path d="M192 0 H202 C246 110 260 230 246 330 C236 400 215 450 195 496 H185 C205 450 226 400 236 330 C250 230 235 110 192 0Z" fill="#ffffff"/>
  </svg>

  <div class="abs apart-band"></div>
  <h2 class="abs heading apart-title">What sets us apart?</h2>

  <div class="feature" style="top:126px">
    <div class="feature-head"><span class="feature-icon"><svg viewBox="0 0 16 16"><circle cx="5" cy="6" r="2.5"/><path d="M5 8.5V13M9 12c3 0 4-2 4-4M11 3l2 2-2 2"/></svg></span>The best routes</div>
    <p class="body-copy">Our routes have been carefully researched and designed to offer a variety of invigorating and rewarding ride options with a combination of world famous routes, signature climbs, and local secrets.</p>
  </div>

  <div class="feature" style="top:226px">
    <div class="feature-head"><span class="feature-icon"><svg viewBox="0 0 16 16"><circle cx="8" cy="5" r="2.5"/><circle cx="4" cy="11" r="2.5"/><circle cx="12" cy="11" r="2.5"/></svg></span>Passion meets expertise</div>
    <p class="body-copy">We've combined decades of experience as an industry-leading tour operator, with our passion as cyclists, to create a program that is not only expertly executed, but also fun, challenging, and unique.</p>
  </div>

  <div class="feature" style="top:323px">
    <div class="feature-head"><span class="feature-icon"><svg viewBox="0 0 16 16"><path d="M8 15V7M8 7 3 3M8 7l5-4M3 3v3M3 3h3M13 3v3M13 3h-3"/></svg></span>Flexibility</div>
    <p class="body-copy">With multiple route options preloaded to your Wayfinder GPS, there's no pressure to adapt your riding style or pace to the group's. You have the flexibility to make each day the adventure that you want.</p>
  </div>

  <div class="abs inside-url">www.velorapedaljourneys.com</div>
  <div class="abs brand-mark inside-brand"><span class="brand-dot"></span></div>

  <div class="abs panel"></div>

  <h2 class="abs heading section-title" style="top:22px">Get moving</h2>
  <p class="abs section-copy" style="top:50px">Our Cycling Adventures are designed for active to avid riders and pay homage to the greatest biking routes in North America. For those about to ride, we salute you.</p>
  <div class="abs rule" style="top:82px"></div>

  <h2 class="abs heading section-title" style="top:94px">Off the beaten roads</h2>
  <p class="abs section-copy" style="top:124px">Motivated by single track, and fueled by microbrews, our Mountain Bike adventures feature an epic mix of world famous rides, and local secrets.</p>
  <div class="abs rule" style="top:155px"></div>

  <h2 class="abs heading section-title" style="top:170px">A premier cycling experience</h2>

  <div class="abs bike-name" style="top:198px"><span>ROAD</span></div>
  <p class="abs section-copy" style="top:213px">When searching for a bike to suit the Velora Pedal Journeys ethos we had to be sure of a few things. For one, it had to perfectly perform regardless of long days on the pavement and detours onto rugged or rocky country roads. This search led us to the Ridgeline Tourer. Not quite a cross-bike but not completely a road bike either, the Tourer is perfect for Velora Pedal Journeys.</p>
  <ul class="abs specs" style="top:266px">
    <li>Carbon fiber fork and frame</li>
    <li>Corsa Elite disc wheels with premier Ridgeline</li>
    <li>Gravelline Pro tires</li>
    <li>Hydraulic disc brakes</li>
    <li>11 speed derailleur system</li>
  </ul>
  <div role="img" aria-label="Photo of a road bike" class="abs bike-photo" style="top:260px"></div>

  <div class="abs bike-name" style="top:342px"><span>MOUNTAIN</span></div>
  <p class="abs section-copy" style="top:357px">The iconic Ridgeline Trailhawk Carbon is the definition of a go everywhere, do everything trail bike. Voted "The #1 trail bike of 2017" by trailnotes.net, the Trailhawk balances technical fun with high speed stability, allowing you to tear up tight turns, or flow through major downhills.</p>
  <ul class="abs specs" style="top:403px">
    <li>Pro-grade 9 carbon fiber trail chassis</li>
    <li>Summit Arc RC fork</li>
    <li>Four-bar suspension</li>
    <li>11-speed Trail groupset</li>
    <li>Frame trapdoor</li>
  </ul>
  <div role="img" aria-label="Photo of a full-suspension mountain bike" class="abs bike-photo" style="top:392px"></div>
</section>

<div class="label label-inside">INSIDE BROCHURE</div>

</body>
</html>
```